Design the World's Greatest Valentine's Day Greeting Card

We're looking for designers who can create the best Valentine's Day greeting card designs in the world. Your design could be could be extra special because it is funny, beautiful, inspiring or original.

Your designs should be able to fit on a standard 4"x6" greeting card. The main design will need to be for the front page (cover) of the card, but you can also include some design for the inside pages if you like.

Multiple winners will be awarded, and will be chosen within 5 days after the contest ends on February 13, 2019.
First Prize: $200
Runners-up: $100 each

The winning card design (or designs) could be recognised as standout designs publicly, as they can be used, by Gigmarten.com, at it sole discretion, in some Gigmarten.com marketing or PR materials.

Let's celebrate Valentine's Day together by showcasing your designs!

```html
<!DOCTYPE html>
<html lang="en">
<head>
<meta charset="utf-8">
<title>I Tolerate You — Valentine's Card</title>
<link rel="stylesheet" href="https://fonts.googleapis.com/css2?family=Patrick+Hand&display=swap">
<style>
  :root {
    --backdrop: #f5b9a0;
    --card-pink: #fde0ec;
    --ink-navy: #1f3b57;
    --heart-red: #e5134f;
  }
  html, body {
    margin: 0;
    padding: 0;
    width: 1200px;
    height: 856px;
    overflow: hidden;
    background: var(--backdrop);
  }
  .canvas {
    position: relative;
    width: 1200px;
    height: 856px;
    display: flex;
    align-items: center;
    justify-content: center;
  }
  .card-front {
    position: relative;
    width: 480px;
    height: 720px;
    background: var(--card-pink);
  }
  .card-message {
    position: absolute;
    left: 0;
    right: 0;
    top: 236px;
    margin: 0;
    text-align: center;
    font-family: "Patrick Hand", "Comic Sans MS", cursive;
    font-weight: 400;
    font-size: 52px;
    line-height: 66px;
    letter-spacing: 3px;
    color: var(--ink-navy);
    text-transform: uppercase;
  }
  .card-heart {
    position: absolute;
    left: 50%;
    top: 446px;
    width: 54px;
    height: 48px;
    transform: translateX(-50%);
  }
  .card-heart path {
    fill: var(--heart-red);
  }
</style>
</head>
<body>
  <main class="canvas">
    <section class="card-front" aria-label="Valentine's card front">
      <h1 class="card-message">I<br>Tolerate<br>You.</h1>
      <svg class="card-heart" viewBox="0 0 54 48" aria-hidden="true">
        <path d="M27 46 C12 35 2 26 2 15 C2 7 8 2 15 2 C20 2 24 5 27 10 C30 5 34 2 39 2 C46 2 52 7 52 15 C52 26 42 35 27 46 Z"/>
      </svg>
    </section>
  </main>
</body>
</html>
```